Website for Kelvara Business Fibre

I need a website done for Kelvara Business Fibre, a new telecommunications business launching in Australia which provides the best internet connectivity for Businesses. It needs to start with the home page, including the logo, layout, colour, font. The rest of the website will follow, around 12 pages.

Ideally the logo will be maximum two colours, with the words Kelvara Business Fibre being the logo rather than another symbol. The emphasis needs to be on the word Kelvara. The design needs to be simple and minimal. I am not sure yet whether the designer will code the page or I will get someone else to do it.

The colours on the slide attached are not meant to be the colours to use, but the layout is close to what I envisage.

```html
<!DOCTYPE html>
<html lang="en">
<head>
<meta charset="utf-8">
<title>Kelvara Business Fibre</title>
<link rel="stylesheet" href="https://fonts.googleapis.com/css2?family=Rajdhani:wght@500;600;700&family=Lato:wght@400;700&family=Roboto:wght@400;500;700&display=swap">
<style>
:root{
  --orange:#ee6a1a;
  --ink:#141414;
  --text:#2b2b2b;
  --white:#ffffff;
  --dark:#262626;
  --footer:#1f1f1f;
  --field:#ffffff;
  --placeholder:#8a8a8a;
}
*{box-sizing:border-box;margin:0;padding:0}
html,body{width:1200px;height:2448px;overflow:hidden;background:var(--white)}
body{position:relative;font-family:'Lato',sans-serif;color:var(--text)}
.abs{position:absolute}

/* header */
.site-header{position:absolute;left:0;top:0;width:1200px;height:127px;background:var(--white)}
.contact-strip{position:absolute;left:0;top:0;width:1200px;height:48px}
.contact-strip .items{position:absolute;top:0;left:520px;height:48px;display:flex;align-items:center;gap:18px;font-family:'Roboto',sans-serif;font-size:15px;color:var(--white)}
.contact-strip .item{display:flex;align-items:center;gap:8px}
.phone-dot{width:28px;height:28px;border-radius:50%;background:var(--white);display:flex;align-items:center;justify-content:center}
.brand{position:absolute;left:100px;top:30px;color:var(--orange);font-family:'Rajdhani',sans-serif;font-weight:600;line-height:1}
.brand .name{font-size:60px;letter-spacing:2px;display:block}
.brand .sub{font-size:21px;letter-spacing:2.5px;display:block;margin-top:2px;text-transform:uppercase}
.main-nav{position:absolute;top:82px;left:425px;display:flex;gap:36px;font-family:'Rajdhani',sans-serif;font-weight:600;font-size:20px;letter-spacing:.5px;color:var(--ink)}
.main-nav .active{color:var(--orange)}

/* hero */
.hero{position:absolute;left:0;top:127px;width:1200px;height:633px}
.hero-photo{position:absolute;inset:0;background:linear-gradient(180deg,#d98a3c 0%,#6b4a3e 18%,#1d2a40 38%,#152036 70%,#0f1a2c 100%)}
.hero-title{position:absolute;left:200px;width:800px;top:156px;text-align:center;color:var(--white);font-family:'Rajdhani',sans-serif;font-weight:700;font-size:36px;line-height:45px}
.hero-edge{position:absolute;left:0;top:0}

/* features */
.why-title{position:absolute;left:0;width:1200px;top:826px;text-align:center;font-family:'Rajdhani',sans-serif;font-weight:700;font-size:50px;color:var(--ink)}
.feature{position:absolute;width:215px;text-align:center}
.feature .icon{width:70px;height:70px;margin:0 auto;border-radius:50%;background:var(--white);box-shadow:0 3px 10px rgba(0,0,0,.15);display:flex;align-items:center;justify-content:center}
.feature h3{font-family:'Roboto',sans-serif;font-weight:500;font-size:20px;color:var(--ink);margin-top:28px;line-height:25px}
.feature p{font-size:15px;line-height:21px;margin-top:8px;color:var(--text)}
.feature h3.accent{color:var(--orange);text-transform:uppercase}
.feature p.price{font-family:'Roboto',sans-serif;font-weight:500;font-size:19px;line-height:22px;color:var(--ink);margin-top:12px}

/* availability */
.availability{position:absolute;left:0;top:1487px;width:1200px;height:724px}
.availability-bg{position:absolute;inset:0;background:linear-gradient(180deg,#2c2c2c 0%,#242424 50%,#1c1c1c 100%)}
.avail-title{position:absolute;left:0;width:1200px;top:181px;text-align:center;color:var(--white);font-family:'Rajdhani',sans-serif;font-weight:700;font-size:44px;line-height:44px}
.field{position:absolute;background:var(--field);font-family:'Roboto',sans-serif;font-weight:500;font-size:14px;color:var(--placeholder);padding:16px 16px;text-transform:uppercase}
.submit{position:absolute;left:523px;top:508px;width:154px;height:62px;border-radius:31px;background:var(--orange);color:var(--white);font-family:'Roboto',sans-serif;font-weight:700;font-size:20px;display:flex;align-items:center;justify-content:center}
.more-info{position:absolute;left:0;width:1200px;top:613px;text-align:center;color:var(--white);font-family:'Roboto',sans-serif;font-weight:500;font-size:25px;line-height:36px}
.phone-pill{display:inline-block;background:var(--orange);border-radius:18px;padding:0 10px;line-height:34px}

/* footer */
.site-footer{position:absolute;left:0;top:2211px;width:1200px;height:237px;background:var(--footer);color:var(--white)}
.footer-nav{position:absolute;left:0;width:1200px;top:63px;display:flex;justify-content:center;gap:29px;font-family:'Rajdhani',sans-serif;font-weight:700;font-size:16px;letter-spacing:.5px}
.copyright{position:absolute;left:0;width:1200px;top:106px;text-align:center;font-family:'Rajdhani',sans-serif;font-weight:500;font-size:14px;letter-spacing:.5px}
.notes{position:absolute;left:0;width:1200px;top:170px;text-align:center;font-family:'Roboto',sans-serif;font-size:12px;line-height:15px}
.live-chat{position:absolute;left:1027px;top:163px;width:130px;height:46px;border-radius:23px;background:var(--orange);display:flex;align-items:center;justify-content:center;font-family:'Rajdhani',sans-serif;font-weight:700;font-size:17px;letter-spacing:.5px}
</style>
</head>
<body>

<header class="site-header">
  <svg class="contact-strip" width="1200" height="48" viewBox="0 0 1200 48"><polygon points="483,0 1200,0 1200,48 513,48" fill="#ee6a1a"/></svg>
  <div class="contact-strip"><div class="items">
    <span class="phone-dot"><svg width="16" height="16" viewBox="0 0 24 24"><path d="M6.6 10.8a15 15 0 0 0 6.6 6.6l2.2-2.2c.3-.3.7-.4 1-.2 1.1.4 2.3.6 3.6.6.6 0 1 .4 1 1V20c0 .6-.4 1-1 1A17 17 0 0 1 3 4c0-.6.4-1 1-1h3.5c.6 0 1 .4 1 1 0 1.3.2 2.5.6 3.6.1.3 0 .7-.2 1z" fill="#ee6a1a"/></svg></span>
    <span class="item"><svg width="17" height="12" viewBox="0 0 17 12"><rect x=".5" y=".5" width="16" height="11" fill="none" stroke="#fff"/><path d="M.5.5l8 6 8-6" fill="none" stroke="#fff"/></svg>sales@kelvarafibre.com.au</span>
    <span class="item"><svg width="17" height="12" viewBox="0 0 17 12"><rect x=".5" y=".5" width="16" height="11" fill="none" stroke="#fff"/><path d="M.5.5l8 6 8-6" fill="none" stroke="#fff"/></svg>support@kelvarafibre.com.au</span>
  </div></div>
  <div class="brand"><span class="name">KELVARA</span><span class="sub">Business Fibre</span></div>
  <nav class="main-nav"><span class="active">HOME</span><span>PRODUCTS</span><span>ABOUT</span><span>NEWS &amp; INSIGHTS</span><span>PARTNERS</span><span>CONTACT</span></nav>
</header>

<section class="hero">
  <div class="hero-photo" role="img" aria-label="City skyline at dusk with glowing network arcs between buildings"></div>
  <h1 class="hero-title">Nexlink Enterprise Ethernet provides businesses of all sizes with superfast, affordable internet over a dedicated fibre - which means it never slows down during peak periods.</h1>
  <svg class="hero-edge" width="1200" height="633" viewBox="0 127 1200 633">
    <polygon points="0,739 971,667 0,757" fill="#ee6a1a"/>
    <polygon points="0,757 971,667 1200,629 1200,760 0,760" fill="#ffffff"/>
  </svg>
</section>

<h2 class="why-title">Why Choose Us?</h2>

<div class="feature" style="left:175px;top:940px">
  <div class="icon"><svg width="30" height="40" viewBox="0 0 30 40"><path d="M18 1L4 23h9l-3 16 16-24h-10z" fill="#ee6a1a"/></svg></div>
  <h3>Fast</h3><p>From 100Mbps upto<br>1Gbps Speed Options</p>
</div>
<div class="feature" style="left:390px;top:940px">
  <div class="icon"><svg width="44" height="40" viewBox="0 0 44 40"><circle cx="22" cy="9" r="7" fill="none" stroke="#ee6a1a" stroke-width="2.5"/><path d="M22 12l-3-3a2 2 0 0 1 3-2 2 2 0 0 1 3 2z" fill="#ee6a1a"/><path d="M2 26l8-6 6 3 6-2 6 2 6-3 8 6-8 8-6-3-6 4-6-4-6 3z" fill="#ee6a1a"/></svg></div>
  <h3>Dedicated fibre</h3><p>doesn't slow down<br>with multiple concurrent<br>users</p>
</div>
<div class="feature" style="left:605px;top:940px">
  <div class="icon"><svg width="36" height="40" viewBox="0 0 36 40"><rect x="2" y="4" width="32" height="6" fill="#ee6a1a"/><rect x="6" y="13" width="24" height="5" fill="#ee6a1a"/><rect x="10" y="21" width="16" height="5" fill="#ee6a1a"/><rect x="16" y="2" width="4" height="36" fill="#fff"/><rect x="17" y="4" width="2" height="34" fill="#ee6a1a"/></svg></div>
  <h3>Symmetric</h3><p>same download and upload<br>speeds, critical for<br>business use</p>
</div>
<div class="feature" style="left:820px;top:940px">
  <div class="icon"><svg width="42" height="42" viewBox="0 0 42 42"><circle cx="21" cy="21" r="19" fill="#ee6a1a"/><g fill="none" stroke="#fff" stroke-width="2"><ellipse cx="21" cy="21" rx="8" ry="19"/><path d="M2 21h38M5 12h32M5 30h32M21 2v38"/></g></svg></div>
  <h3>Widely Available</h3><p>to 1.5M sites around Australia<br>including metro, regional<br>and remote locations</p>
</div>

<div class="feature" style="left:175px;top:1188px">
  <div class="icon"><svg width="36" height="42" viewBox="0 0 36 42"><path d="M18 2l15 6v12c0 10-7 17-15 20C10 37 3 30 3 20V8z" fill="none" stroke="#ee6a1a" stroke-width="3"/><path d="M11 21l5 5 9-10" fill="none" stroke="#ee6a1a" stroke-width="3"/></svg></div>
  <h3>Reliable</h3><p style="margin-top:22px">Designed for up to 99.95%<br>network availability with<br>4G back up option</p>
</div>
<div class="feature" style="left:390px;top:1188px">
  <div class="icon"><svg width="44" height="42" viewBox="0 0 44 42"><g fill="#ee6a1a"><circle cx="22" cy="20" r="5"/><circle cx="11" cy="24" r="4"/><circle cx="33" cy="24" r="4"/><path d="M13 40c0-8 4-12 9-12s9 4 9 12z"/><path d="M3 40c0-6 3-9 8-9 2 0 3 1 4 2-2 2-3 4-3 7z"/><path d="M41 40c0-6-3-9-8-9-2 0-3 1-4 2 2 2 3 4 3 7z"/><path d="M22 1l2 4 4 .5-3 3 1 4-4-2-4 2 1-4-3-3 4-.5z"/><path d="M9 6l1.5 3 3 .5-2 2 .5 3-3-1.5-3 1.5.5-3-2-2 3-.5z"/><path d="M35 6l1.5 3 3 .5-2 2 .5 3-3-1.5-3 1.5.5-3-2-2 3-.5z"/></g></svg></div>
  <h3>Expert Support</h3><p style="margin-top:22px">100% Australian<br>team with 24x7 service</p>
</div>
<div class="feature" style="left:605px;top:1188px">
  <div class="icon"><svg width="38" height="38" viewBox="0 0 38 38"><path d="M19 3v20M11 15l8 8 8-8" fill="none" stroke="#ee6a1a" stroke-width="4"/><path d="M3 24v10h32V24" fill="none" stroke="#ee6a1a" stroke-width="4"/></svg></div>
  <h3>No upfont<br>build cost</h3><p style="margin-top:4px">same download and<br>upload speeds, critical<br>for business use</p>
</div>
<div class="feature" style="left:820px;top:1188px">
  <div class="icon"><svg width="40" height="42" viewBox="0 0 40 42"><circle cx="22" cy="14" r="8" fill="#ee6a1a"/><text x="22" y="19" text-anchor="middle" font-family="Roboto, sans-serif" font-weight="700" font-size="12" fill="#fff">$</text><path d="M22 1v3M15 3l1 2M29 3l-1 2" stroke="#ee6a1a" stroke-width="2"/><path d="M3 28h8l8 3h10l6-4 2 2-8 7H15l-4-2H3z" fill="#ee6a1a"/></svg></div>
  <h3 class="accent">Affordable</h3><p class="price">starting at $X per<br>month</p>
</div>

<section class="availability">
  <div class="availability-bg" role="img" aria-label="Dark monochrome city skyline overlaid with a network of connected points"></div>
  <svg class="abs" style="left:0;top:0" width="1200" height="100" viewBox="0 0 1200 100">
    <polygon points="0,0 1200,0 1200,0 0,98" fill="#ffffff"/>
    <polygon points="0,0 1200,0 656,44 0,98" fill="#ffffff"/>
    <polygon points="0,44 656,44 0,98" fill="#ee6a1a"/>
    <polygon points="0,0 1200,0 656,44 0,44" fill="#ffffff"/>
  </svg>
  <h2 class="avail-title">Find out if Nexlink Enterprise Ethernet is<br>available at your business location.</h2>
  <div class="field" style="left:174px;top:326px;width:268px;height:45px">Name</div>
  <div class="field" style="left:459px;top:326px;width:268px;height:45px">Phone</div>
  <div class="field" style="left:746px;top:326px;width:276px;height:45px">Email</div>
  <div class="field" style="left:174px;top:399px;width:849px;height:136px">Message</div>
  <div class="submit">SUBMIT</div>
  <p class="more-info">For more information, call <span class="phone-pill">1300 555 019</span> or<br>email sales@kelvarafibre.com.au</p>
</section>

<footer class="site-footer">
  <nav class="footer-nav"><span>HOME</span><span>PRODUCTS</span><span>ABOUT</span><span>NEWS &amp; INSIGHTS</span><span>PARTNERS</span><span>CONTACT</span></nav>
  <p class="copyright">COPY RIGHT © 2022 KELVARA BUSINESS FIBRE. ALL RIGHTS RESERVED</p>
  <p class="notes">* Actual speed capped at 952Mbps and may vary due to various equipment and network factors<br>** Other contract term options available, however No upfront build starts on 3 year contract</p>
  <div class="live-chat">LIVE CHAT</div>
</footer>

</body>
</html>
```